Creating a label for germicidal disposable wipes.

I need to create a label to put on our containers of germicidal disposable wipes. I am attaching an example of another germicidal wipe that I would like a similar format but more customized to look like my companies.

```html
<!DOCTYPE html>
<html lang="en">
<head>
<meta charset="utf-8">
<title>SaniVex Germicidal Wipes Label</title>
<link rel="stylesheet" href="https://fonts.googleapis.com/css2?family=Montserrat:wght@500;600;700;800&family=Open+Sans:wght@600&display=swap">
<style>
  :root {
    --ink: #333333;
    --green: #2aa84a;
    --green-deep: #1f9444;
    --navy: #2b3a8c;
    --white: #ffffff;
    --edge: #d6d6d6;
  }
  * { margin: 0; padding: 0; box-sizing: border-box; }
  html, body { width: 1200px; height: 1200px; overflow: hidden; background: var(--white); }
  .canvas { position: relative; width: 1200px; height: 1200px; background: var(--white); font-family: "Montserrat", sans-serif; color: var(--ink); }

  .label {
    position: absolute; left: 102px; top: 297px; width: 998px; height: 606px;
    border-radius: 60px; overflow: hidden; background: var(--white);
    border: 1.5px solid var(--edge);
    box-shadow: 0 2px 4px rgba(0,0,0,0.12);
  }
  .label__band {
    position: absolute; left: 0; top: 0; width: 100%; height: 130px;
    background: linear-gradient(100deg, var(--navy) 0%, var(--green) 18%, var(--green) 28%, var(--green-deep) 40%, var(--navy) 62%, var(--green) 88%, var(--green) 100%);
  }
  .label__brandbox {
    position: absolute; left: 198px; top: 0; width: 262px; height: 130px;
    background: var(--white);
    display: flex; align-items: center; justify-content: center; gap: 12px;
  }
  .brand__dot { width: 30px; height: 30px; border-radius: 50%; background: var(--green); }
  .brand__name { font-weight: 700; font-size: 38px; color: var(--ink); letter-spacing: 1px; }

  .product { position: absolute; left: 90px; top: 135px; width: 420px; }
  .product__name { font-weight: 800; font-size: 82px; line-height: 1; color: #3a3a3a; letter-spacing: -1px; text-align: center; }
  .product__type { font-weight: 500; font-size: 30px; letter-spacing: 2.5px; text-align: center; margin-top: 4px; color: #3a3a3a; }
  .product__use { font-weight: 700; font-size: 26px; color: var(--green); text-align: center; margin-top: 2px; letter-spacing: 0.5px; }

  .claims { position: absolute; left: 96px; top: 300px; display: flex; gap: 12px; }
  .claim { width: 94px; height: 94px; }

  .ingredients { position: absolute; left: 90px; top: 398px; font-size: 13px; line-height: 18.5px; font-weight: 500; color: #222; }
  .ingredients__title { font-weight: 700; }

  .warning { position: absolute; left: 90px; top: 478px; width: 440px; }
  .warning__kids { font-weight: 700; font-size: 23px; line-height: 26px; color: #3a3a3a; }
  .warning__row { display: flex; align-items: flex-start; gap: 10px; }
  .warning__word { font-weight: 800; font-size: 33px; line-height: 34px; color: #3a3a3a; }
  .warning__note { font-weight: 600; font-size: 15px; line-height: 15px; color: #3a3a3a; margin-top: 3px; }

  .contents { position: absolute; left: 90px; top: 544px; width: 460px; }
  .contents__count { font-weight: 700; font-size: 19px; color: var(--green); }
  .contents__size { font-weight: 500; font-size: 11.5px; color: #333; margin-left: 4px; }
  .contents__weight { font-weight: 600; font-size: 14px; color: #333; margin-top: 1px; }

  .directions {
    position: absolute; left: 535px; top: 148px; width: 370px; height: 430px; overflow: hidden;
    font-family: "Open Sans", sans-serif; font-weight: 600; font-size: 11px; line-height: 14.7px; color: #222;
  }
</style>
</head>
<body>
<div class="canvas">
  <div class="label">
    <div class="label__band"></div>
    <div class="label__brandbox">
      <span class="brand__dot"></span>
      <span class="brand__name">ORVANE</span>
    </div>

    <div class="product">
      <h1 class="product__name">SaniVex</h1>
      <p class="product__type">GERMICIDAL WIPES</p>
      <p class="product__use">SURFACE DESINFECTANT</p>
    </div>

    <div class="claims">
      <svg class="claim" viewBox="0 0 94 94" aria-label="Disinfects in 2 minutes">
        <defs>
          <linearGradient id="ringGrad" x1="0" y1="0" x2="1" y2="1">
            <stop offset="0" stop-color="#2aa84a"/><stop offset="1" stop-color="#2b3a8c"/>
          </linearGradient>
        </defs>
        <circle cx="47" cy="47" r="44" fill="none" stroke="url(#ringGrad)" stroke-width="5"/>
        <circle cx="47" cy="47" r="28" fill="#2b3a8c"/>
        <text x="47" y="55" text-anchor="middle" font-family="Montserrat, sans-serif" font-weight="800" font-size="26" fill="#fff">2</text>
        <text x="47" y="83" text-anchor="middle" font-family="Montserrat, sans-serif" font-weight="700" font-size="7" fill="#2b3a8c">MINUTES</text>
      </svg>
      <svg class="claim" viewBox="0 0 94 94" aria-label="Not a skin or baby wipe">
        <circle cx="47" cy="47" r="44" fill="none" stroke="url(#ringGrad)" stroke-width="5"/>
        <circle cx="47" cy="47" r="28" fill="#2b3a8c"/>
        <line x1="33" y1="61" x2="61" y2="33" stroke="#fff" stroke-width="5" stroke-linecap="round"/>
        <circle cx="47" cy="47" r="17" fill="none" stroke="#fff" stroke-width="4"/>
      </svg>
      <svg class="claim" viewBox="0 0 94 94" aria-label="Do not flush">
        <circle cx="47" cy="47" r="44" fill="none" stroke="url(#ringGrad)" stroke-width="5"/>
        <circle cx="47" cy="47" r="28" fill="#2b3a8c"/>
        <line x1="36" y1="36" x2="58" y2="58" stroke="#fff" stroke-width="5" stroke-linecap="round"/>
        <line x1="58" y1="36" x2="36" y2="58" stroke="#fff" stroke-width="5" stroke-linecap="round"/>
      </svg>
    </div>

    <div class="ingredients">
      <p class="ingredients__title">ACTIVE INGREDIENTS:</p>
      <p>Isopropyl Alcohol</p>
      <p>Alkyl C12 -28 dimethyl ammonium chloride</p>
      <p>Alkyl C12 -28 dimethyl ethyl benzyl ammonium chloride</p>
    </div>

    <div class="warning">
      <p class="warning__kids">KEEP OUT OF REACH OF CHILDREN</p>
      <div class="warning__row">
        <p class="warning__word">WARNING</p>
        <p class="warning__note">See back panel for additional<br>precautionary statements</p>
      </div>
    </div>

    <div class="contents">
      <p><span class="contents__count">CONTAINS: 160 Wipes</span><span class="contents__size">6 x 6.75 in (15.2 x 17.1 cm)</span></p>
      <p class="contents__weight">Net Wt. 1 lb &nbsp;13 oz (833g)</p>
    </div>

    <div class="directions">
      <p>Lorem ipsum dolor sit amet, consectetuer adipiscing elit, sed diam nonummy nibh euismod tincidunt ut laoreet dolore magna aliquam erat volutpat. Ut wisi enim ad minim veniam, quis nostrud exercitation ullamcorper suscipit lobortis nisl ut aliquip ex ea commodo consequat. Duis autem vel eum iriure dolor in hendrerit in vulputate velit esse molestie consequat, vel illum dolore eu feugiat nulla facilisis at vero eros et accumsan et iusto odio dignissim qui blandit praesent luptatum zzril delenit augue duis dolore te feugait nulla facilisi.</p>
      <p>Lorem ipsum dolor sit amet, consectetuer adipiscing elit, sed diam nonummy nibh euismod tincidunt ut laoreet dolore magna aliquam erat volutpat. Ut wisi enim ad minim veniam, quis nostrud exercitation ullamcorper suscipit lobortis nisl ut aliquip ex ea commodo consequat.</p>
      <p>Lorem ipsum dolor sit amet, consectetuer adipiscing elit, sed diam nonummy nibh euismod tincidunt ut laoreet dolore magna aliquam erat volutpat. Ut wisi enim ad minim veniam, quis nostrud exercitation ullamcorper suscipit lobortis nisl ut aliquip ex ea commodo consequat. Duis autem vel eum iriure dolor in hendrerit in vulputate velit esse molestie consequat, vel illum dolore eu feugiat nulla facilisis at vero eros et accumsan et iusto odio dignissim qui blandit praesent luptatum zzril delenit augue duis dolore te feugait nulla facilisi.</p>
      <p>Lorem ipsum dolor sit amet, consectetuer adipiscing elit, sed diam nonummy nibh euismod tincidunt ut laoreet dolore magna aliquam erat volutpat. Ut wisi enim ad minim</p>
    </div>
  </div>
</div>
</body>
</html>
```